Granite, Brass and Shingle Roofing LLC needs a new business card

I need a new business card because I have a new address.
I do slate copper and tile roofs. My webpage is: www.granitebrassandshingleroofing.com

```html
<!DOCTYPE html>
<html lang="en">
<head>
<meta charset="utf-8">
<title>Granite, Brass and Shingle Roofing LLC — Business Card</title>
<link href="https://fonts.googleapis.com/css2?family=Arimo:wght@400;700&display=swap" rel="stylesheet">
<style>
  :root {
    --page: #e4e4e2;
    --card: #26272a;
    --card-deep: #1f2022;
    --edge: #3c7fb0;
    --accent: #4b9bd0;
    --text: #ffffff;
    --muted: #d9d9d9;
    --emboss: #3a3b3f;
    --rule: #cfcfcf;
  }
  * { margin: 0; padding: 0; box-sizing: border-box; }
  html, body {
    width: 1200px; height: 801px; overflow: hidden;
    background: var(--page);
    font-family: "Arimo", Arial, sans-serif;
  }
  .stage {
    width: 1200px; height: 801px;
    display: flex; align-items: center; justify-content: center; gap: 50px;
  }
  .card {
    width: 525px; height: 300px;
    background: linear-gradient(135deg, var(--card) 0%, var(--card-deep) 100%);
    border-bottom: 4px solid var(--edge);
    border-left: 2px solid var(--edge);
    position: relative;
    color: var(--text);
  }
  /* front */
  .card-front { display: flex; align-items: center; }
  .brand {
    width: 245px; display: flex; align-items: center; gap: 10px;
    padding-left: 34px;
  }
  .brand-mark { width: 22px; height: 22px; background: var(--accent); flex: none; }
  .brand-name {
    font-size: 17px; font-weight: 700; line-height: 1.2; color: var(--accent);
  }
  .divider {
    width: 1px; height: 170px; background: var(--rule); margin: 0 22px 0 4px;
  }
  .contact { font-size: 12.5px; line-height: 1.45; }
  .contact-name {
    color: var(--accent); font-weight: 700; font-size: 17px;
    text-transform: uppercase; letter-spacing: .3px;
  }
  .contact-role { color: var(--muted); margin-bottom: 12px; font-size: 13px; }
  .contact-address { margin-bottom: 12px; }
  .contact-line { display: flex; align-items: center; gap: 7px; }
  .contact-line svg { width: 12px; height: 12px; flex: none; fill: var(--accent); }
  /* back */
  .card-back { display: flex; align-items: center; justify-content: center; gap: 14px; }
  .back-mark { width: 34px; height: 34px; background: var(--emboss); }
  .back-name {
    font-size: 30px; font-weight: 700; line-height: 1.15; color: var(--emboss);
  }
</style>
</head>
<body>
<main class="stage">
  <section class="card card-front">
    <div class="brand">
      <span class="brand-mark"></span>
      <span class="brand-name">Granite, Brass &amp; Shingle<br>Roofing</span>
    </div>
    <div class="divider"></div>
    <div class="contact">
      <p class="contact-name">Laszlo (Les) Varga</p>
      <p class="contact-role">Owner</p>
      <p class="contact-address">2871 Millbrook Rd.<br>Millbrook, OH 44990</p>
      <p class="contact-line">
        <svg viewBox="0 0 24 24" aria-hidden="true"><path d="M6.6 10.8a15.1 15.1 0 0 0 6.6 6.6l2.2-2.2c.3-.3.7-.4 1-.2 1.1.4 2.3.6 3.6.6.6 0 1 .4 1 1V20c0 .6-.4 1-1 1A17 17 0 0 1 3 4c0-.6.4-1 1-1h3.5c.6 0 1 .4 1 1 0 1.3.2 2.5.6 3.6.1.3 0 .7-.2 1z"/></svg>
        (440) 555-0186
      </p>
      <p class="contact-line">
        <svg viewBox="0 0 24 24" aria-hidden="true"><path d="M2 5h20v14H2zm2 2v.5l8 5 8-5V7l-8 5z"/></svg>
        gbsroofingllc@mail.com
      </p>
      <p class="contact-line">
        <svg viewBox="0 0 24 24" aria-hidden="true"><circle cx="12" cy="12" r="10"/></svg>
        www.granitebrassandshingleroofing.com
      </p>
    </div>
  </section>

  <section class="card card-back">
    <span class="back-mark"></span>
    <span class="back-name">Granite, Brass &amp; Shingle<br>Roofing</span>
  </section>
</main>
</body>
</html>
```